Book Cover for Political Biography

Back round color, darker green.

This book is a political biography of Mr. Ter Haar Veldt who was a prominent politician in Curacao.

Looking for a modern toward the conservative look. The attached images can be used as place holders, we will get hi resolution ones to replace.

Book Title:
Mr. Dr. Anselm ter Haar Veldt: Pionier voor het Bestuurlijke Zelfbeschikking der Westelijke Eilanden

Name Author:
drs. K.J. (Thibault) Wessinghe MBA

Please leave space on the back for book description (one paragraph) and author biography (short paragraph)

```html
<!DOCTYPE html>
<html lang="nl">
<head>
<meta charset="utf-8">
<title>Mr. Dr. Anselm ter Haar Veldt – Boekomslag</title>
<link rel="stylesheet" href="https://fonts.googleapis.com/css2?family=Big+Shoulders+Display:wght@100;200&family=Tinos:wght@400;700&display=swap">
<style>
  :root {
    --green-deep: #1a361a;
    --green-mid: #2a5628;
    --green-soft: #3b6a36;
    --spine-green: #173216;
    --spine-edge: #0e220e;
    --ink-white: #ffffff;
    --ink-shadow: rgba(0, 0, 0, 0.7);
    --front-photo-light: #a7a496;
    --front-photo-mid: #6e6d60;
    --front-photo-dark: #3d3f34;
    --back-photo-light: #d6e3cf;
    --back-photo-mid: #8fa889;
    --back-photo-dark: #3d5a38;
    --portrait-light: #c9c9c4;
    --portrait-dark: #6d6d69;
  }
  html, body {
    margin: 0;
    padding: 0;
    width: 1200px;
    height: 900px;
    overflow: hidden;
    background: var(--green-deep);
  }
  .cover-spread {
    position: relative;
    width: 1200px;
    height: 900px;
    overflow: hidden;
    background: radial-gradient(ellipse at 50% 65%, var(--green-soft) 0%, var(--green-mid) 45%, var(--green-deep) 100%);
    font-family: "Tinos", "Times New Roman", serif;
    color: var(--ink-white);
  }
  .back-cover, .spine, .front-cover {
    position: absolute;
    top: 0;
    height: 900px;
  }
  .back-cover { left: 0; width: 540px; }
  .spine {
    left: 540px;
    width: 128px;
    background: linear-gradient(90deg, var(--spine-edge) 0%, var(--spine-green) 12%, var(--green-mid) 50%, var(--spine-green) 88%, var(--spine-edge) 100%);
  }
  .front-cover { left: 668px; width: 532px; }

  .back-photo {
    position: absolute;
    left: 0; top: 0;
    width: 540px; height: 440px;
    background:
      linear-gradient(180deg, rgba(42, 86, 40, 0) 0%, rgba(42, 86, 40, 0) 45%, rgba(42, 86, 40, 0.85) 80%, var(--green-mid) 100%),
      linear-gradient(90deg, var(--back-photo-mid) 0%, var(--back-photo-light) 12%, var(--back-photo-dark) 30%, var(--back-photo-mid) 50%, var(--back-photo-dark) 62%, var(--back-photo-light) 78%, var(--back-photo-mid) 100%);
  }
  .front-photo {
    position: absolute;
    left: 0; top: 0;
    width: 532px; height: 620px;
    background:
      linear-gradient(180deg, rgba(42, 86, 40, 0) 0%, rgba(42, 86, 40, 0) 50%, rgba(42, 86, 40, 0.8) 78%, var(--green-mid) 100%),
      linear-gradient(90deg, var(--front-photo-mid) 0%, var(--front-photo-dark) 12%, var(--front-photo-light) 32%, var(--front-photo-mid) 52%, var(--front-photo-light) 70%, var(--front-photo-light) 88%, var(--front-photo-mid) 100%);
  }
  .author-portrait {
    position: absolute;
    left: 46px; top: 702px;
    width: 96px; height: 156px;
    background: linear-gradient(180deg, var(--portrait-light) 0%, var(--portrait-dark) 100%);
  }

  .title-art {
    position: absolute;
    overflow: visible;
  }
  .title-art text {
    font-family: "Big Shoulders Display", "Oswald", sans-serif;
    font-weight: 100;
    fill: var(--ink-white);
    filter: drop-shadow(2px 3px 2px var(--ink-shadow));
  }
  .back-title { left: 60px; top: 282px; }
  .front-title { left: 0; top: 368px; }

  .subtitle {
    position: absolute;
    margin: 0;
    text-align: center;
    line-height: 1.2;
    text-shadow: 1px 2px 2px var(--ink-shadow);
  }
  .back-subtitle { left: 30px; width: 500px; top: 330px; font-size: 19px; }
  .front-subtitle { left: 0; width: 532px; top: 670px; font-size: 21px; }

  .spine-title {
    position: absolute;
    left: 0; top: 0;
  }
  .spine-author {
    position: absolute;
    left: 0; width: 128px;
    top: 853px;
    margin: 0;
    font-size: 8px;
    font-weight: 700;
    text-align: center;
  }
  .front-author {
    position: absolute;
    left: 0; width: 532px;
    top: 838px;
    margin: 0;
    font-size: 21px;
    font-weight: 400;
    text-align: center;
    text-shadow: 1px 2px 2px var(--ink-shadow);
  }
</style>
</head>
<body>
<main class="cover-spread">

  <section class="back-cover">
    <div class="back-photo" role="img" aria-label="Archieffoto: groep mannen in pakken bij een bijeenkomst"></div>
    <svg class="title-art back-title" width="460" height="50" viewBox="0 0 460 50">
      <text x="0" y="42" font-size="52" textLength="445" lengthAdjust="spacingAndGlyphs">MR. DR. ANSELM TERHAARVELDT:</text>
    </svg>
    <p class="subtitle back-subtitle">Pionier voor het Bestuurlijke Zelfbeschikking der<br>Westelijke Eilanden</p>
    <div class="author-portrait" role="img" aria-label="Portretfoto van de auteur"></div>
  </section>

  <section class="spine">
    <svg class="spine-title" width="128" height="900" viewBox="0 0 128 900">
      <g transform="translate(62 112) rotate(90)">
        <text x="0" y="0" font-size="50" textLength="635" lengthAdjust="spacingAndGlyphs"
              style="font-family:'Big Shoulders Display','Oswald',sans-serif;font-weight:100;fill:#fff;">MR. DR. ANSELM TERHAARVELDT:</text>
      </g>
      <g transform="translate(18 120) rotate(90)">
        <text x="0" y="0" font-size="19" textLength="625" lengthAdjust="spacingAndGlyphs"
              style="font-family:'Tinos','Times New Roman',serif;fill:#fff;">Pionier voor het Bestuurlijke Zelfbeschikking der Westelijke Eilanden</text>
      </g>
    </svg>
    <p class="spine-author">drs. K.J. (Thibault) Wessinghe MBA</p>
  </section>

  <section class="front-cover">
    <div class="front-photo" role="img" aria-label="Archieffoto: twee mannen in gesprek aan tafel"></div>
    <svg class="title-art front-title" width="532" height="300" viewBox="0 0 532 300">
      <text x="52" y="120" font-size="140" textLength="400" lengthAdjust="spacingAndGlyphs">MR. DR. ANSELM</text>
      <text x="14" y="290" font-size="140" textLength="490" lengthAdjust="spacingAndGlyphs">TERHAARVELDT:</text>
    </svg>
    <p class="subtitle front-subtitle">Pionier voor het Bestuurlijke Zelfbeschikking der<br>Westelijke Eilanden</p>
    <p class="front-author">drs. K.J. (Thibault) Wessinghe MBA</p>
  </section>

</main>
</body>
</html>
```